diesel mechanic business card design

summit diesel is a new and upcoming business we are looking for some bad ass designs to help get us started we offer 24 hour road service, off road recovery, welding and custom fabrications we are diesel mechanics so our design should be bold and eye catching flames wrenches engine parts are cool we work in an industrial environment around heavy trucks and equipment this in not a quikk oilery we fix it all nothing is to big or to small the colors red and black are always a plus but we are open to anything you guys can come up with ready set go

Target Market(s)

other small business primarily trucking and transportation companys

Industry/Entity Type

Business

Contact Information for Business Card

company name Sumit diesel truck & trailer repair / address 14 rear north wendell ave Ridgeford OH 18642 / ownersAdam DeLuccie 570-555-0148 / Glenn Wasowicz 570-555-0193 E mail brianforsythe@mailbox-example.com fax 570-555-0127

Requirements
Nice to have
• industrial modern design
Should not have
• rainbows butterfly's unicorns or cupcakes

```html
<!DOCTYPE html>
<html lang="en">
<head>
<meta charset="utf-8">
<title>Summit Diesel – Business Card</title>
<link rel="stylesheet" href="https://fonts.googleapis.com/css2?family=Oswald:wght@400;500;600&display=swap">
<style>
  :root {
    --stage: #1c1c1c;
    --card-dark: #0e0e0e;
    --card-light: #ffffff;
    --ink: #2a2a2a;
    --orange: #e8892c;
    --red: #e0392a;
    --yellow: #f7c23a;
    --front-text: #c9c9c9;
  }
  * { box-sizing: border-box; margin: 0; padding: 0; }
  html, body {
    width: 1200px; height: 871px; overflow: hidden;
    background: var(--stage);
    font-family: "Oswald", sans-serif;
  }
  .stage {
    width: 1200px; height: 871px;
    display: flex; flex-direction: column;
    align-items: center; justify-content: center; gap: 40px;
  }
  .card {
    width: 680px; height: 388px;
    position: relative;
    box-shadow: 0 12px 30px rgba(0,0,0,.5);
  }

  /* Front */
  .card--front {
    background: var(--card-dark);
    display: flex; flex-direction: column; align-items: center;
    padding-top: 80px;
  }
  .brand { display: flex; align-items: center; gap: 18px; }
  .brand__square { width: 34px; height: 34px; background: var(--orange); }
  .brand__name {
    font-weight: 400; letter-spacing: .45em;
    text-transform: uppercase; white-space: nowrap;
  }
  .card--front .brand__name { font-size: 56px; line-height: 1; color: #e6e6e6; }
  .tagline {
    margin-top: 22px;
    font-size: 22px; font-weight: 600; letter-spacing: .06em;
    color: var(--orange); text-transform: uppercase;
  }
  .owners {
    margin-top: 60px;
    font-size: 16px; font-weight: 500; letter-spacing: .06em;
    color: var(--front-text); text-transform: uppercase; white-space: nowrap;
  }
  .owners .phone { color: var(--orange); }
  .owners .divider { margin: 0 12px; }

  /* Back */
  .card--back {
    background: var(--card-light);
    display: flex; align-items: center;
  }
  .card--back .brand {
    width: 270px; flex-direction: column; gap: 16px;
  }
  .card--back .brand__square { width: 60px; height: 60px; }
  .card--back .brand__name { font-size: 36px; line-height: 1; color: var(--ink); padding-left: .45em; }
  .rule {
    width: 3px; height: 240px; flex: none;
    background: linear-gradient(var(--yellow), var(--orange), var(--red));
  }
  .details { padding-left: 26px; padding-right: 16px; color: var(--ink); }
  .details__names { font-size: 20px; font-weight: 600; letter-spacing: .04em; white-space: nowrap; }
  .details__role { font-size: 16px; color: var(--orange); letter-spacing: .12em; margin-bottom: 10px; }
  .contact {
    list-style: none; display: flex; flex-direction: column; gap: 6px;
    font-size: 16px; font-weight: 500; letter-spacing: .03em; white-space: nowrap;
  }
  .contact li { display: flex; align-items: center; gap: 10px; }
  .contact svg { width: 16px; height: 16px; flex: none; fill: var(--orange); }
</style>
</head>
<body>
<main class="stage">

  <section class="card card--front">
    <div class="brand">
      <span class="brand__square"></span>
      <span class="brand__name">Summit</span>
    </div>
    <p class="tagline">Diesel Truck &amp; Trailer Repair</p>
    <p class="owners">
      Brian Forsythe - <span class="phone">570-555-0148</span>
      <span class="divider">|</span>
      Glenn Wasowicz - <span class="phone">570-555-0193</span>
    </p>
  </section>

  <section class="card card--back">
    <div class="brand">
      <span class="brand__square"></span>
      <span class="brand__name">Summit</span>
    </div>
    <div class="rule"></div>
    <div class="details">
      <p class="details__names">Brian Forsythe I Glenn Wasowicz</p>
      <p class="details__role">owner</p>
      <ul class="contact">
        <li>
          <svg viewBox="0 0 16 16"><path d="M8 1a5 5 0 0 0-5 5c0 3.5 5 9 5 9s5-5.5 5-9a5 5 0 0 0-5-5zm0 7a2 2 0 1 1 0-4 2 2 0 0 1 0 4z"/></svg>
          14 Rear north Wendell Ave Ridgeford OH 18642
        </li>
        <li>
          <svg viewBox="0 0 16 16"><path d="M1 3h14v10H1z M2 4l6 5 6-5" fill="none" stroke="#e8892c" stroke-width="1.5"/></svg>
          brianforsythe@mailbox-example.com
        </li>
        <li>
          <svg viewBox="0 0 16 16"><path d="M4 1h8v4H4z M1 6h14v7h-3v2H4v-2H1z M5 10h6v4H5z" fill-rule="evenodd"/></svg>
          570-555-0127
        </li>
      </ul>
    </div>
  </section>

</main>
</body>
</html>
```